Business card for Eyelash extension salon in Beverly Hills,California USA

We need new business card for our salon in Beverly Hills. The salon name is 'Lashvora' . We would like to have...Business name: Lashvora Name of person: will provide later Address 6812 N.Calder Ridge Ave Beverly Hills , CA 90210 Phone: will provide later (Text only) Web: www.lashvorastudio-demo.com Instagram icon, Facebook icon follow us for seasonal campaign and news @lashvorastudiodemo Design should look elegant, high-end, clean, simple, cohesive with my brand. Please refer my brand board. Business name color will be metallic bronzy color. Im thinking grey background or white background. Thanks

Target Market(s)

25-35. Gender neutral. People who are in Entertainment business industry.
This is High-end Eyelash extension salon in Beverly Hills

Industry/Entity Type

Beauty Salon

Contact Information for Business Card

Business name: Lashvora
Name of person: will provide later
Address 6812 N.Calder Ridge Ave Beverly Hills , CA 90210
Phone: will provide later (Text only)
Web: www.lashvorastudio-demo.com
Instagram icon, Facebook icon
follow us for seasonal campaign and news @lashvorastudiodemo

Requirements
Must have
• Beautiful, elegant, clean and simple look but very attractive and modern
Should not have
• We don't like too clutter, too busy designs.

```html
<!DOCTYPE html>
<html lang="en">
<head>
<meta charset="utf-8">
<title>Lashvora Business Card</title>
<link href="https://fonts.googleapis.com/css2?family=Gilda+Display&family=Libre+Caslon+Text:wght@400&family=Josefin+Sans:wght@400&display=swap" rel="stylesheet">
<style>
  :root {
    --stage: #2c2c2c;
    --paper: #ffffff;
    --bronze: #8b6a51;
    --bronze-deep: #7c5c44;
    --ink: #1f1f1f;
    --on-bronze: #ffffff;
  }
  * { margin: 0; padding: 0; box-sizing: border-box; }
  html, body {
    width: 1200px; height: 930px; overflow: hidden;
    background: var(--stage);
  }
  .stage { position: relative; width: 1200px; height: 930px; }

  .card {
    position: absolute;
    left: 318px;
    width: 564px;
    height: 323px;
  }
  .card--front { top: 125px; background: var(--paper); }
  .card--back  { top: 514px; background: var(--bronze); }

  /* Brand name */
  .brand {
    position: absolute;
    font-family: "Gilda Display", serif;
    font-weight: 400;
    line-height: 1;
    white-space: nowrap;
  }
  .brand__name { display: block; }
  .brand__place {
    display: block;
    font-family: "Josefin Sans", sans-serif;
    letter-spacing: 0.22em;
  }
  .card--front .brand { left: 27px; top: 48px; color: var(--bronze); }
  .card--front .brand__name { font-size: 50px; }
  .card--front .brand__place { font-size: 6.5px; margin: 12px 0 0 88px; }

  .card--back .brand {
    left: 0; right: 0; top: 104px; text-align: center; color: var(--on-bronze);
  }
  .card--back .brand__name { font-size: 86px; }
  .card--back .brand__place { font-size: 10px; margin: 18px 0 0 60px; }

  /* Person */
  .person {
    position: absolute;
    right: 30px;
    top: 162px;
    text-align: right;
  }
  .person__name {
    font-family: "Libre Caslon Text", serif;
    font-size: 27px;
    color: var(--bronze-deep);
    line-height: 1;
  }
  .person__role {
    font-family: "Gilda Display", serif;
    font-size: 13px;
    color: var(--ink);
    margin-top: 3px;
  }

  .divider {
    position: absolute;
    left: 27px; right: 30px; top: 226px;
    height: 1.5px;
    background: var(--bronze);
  }

  .contact, .address {
    position: absolute;
    font-family: "Gilda Display", serif;
    font-size: 14px;
    color: var(--ink);
    line-height: 18.5px;
    list-style: none;
  }
  .contact { left: 27px; top: 247px; }
  .contact__item { display: flex; align-items: center; }
  .contact__icon {
    width: 9px; height: 9px; margin-right: 8px; flex: none;
    fill: none; stroke: var(--bronze); stroke-width: 1.2;
  }
  .address { right: 30px; top: 266px; text-align: right; }
</style>
</head>
<body>
<main class="stage">

  <section class="card card--front" aria-label="Business card front">
    <div class="brand">
      <span class="brand__name">Lashvora</span>
      <span class="brand__place">BEVERLY HILLS</span>
    </div>

    <div class="person">
      <p class="person__name">Elena R. Marsh</p>
      <p class="person__role">Director</p>
    </div>

    <div class="divider"></div>

    <ul class="contact">
      <li class="contact__item">
        <svg class="contact__icon" viewBox="0 0 10 10" aria-hidden="true"><path d="M2.2 1 L3.6 1 L4.2 3 L3.2 3.8 Q4.2 5.8 6.2 6.8 L7 5.8 L9 6.4 L9 7.8 Q9 9 7.6 9 Q1 8 1 2.4 Q1 1 2.2 1 Z" fill="var(--bronze)" stroke="none"/></svg>
        310.555.0142
      </li>
      <li class="contact__item">
        <svg class="contact__icon" viewBox="0 0 10 10" aria-hidden="true"><rect x="0.8" y="2" width="8.4" height="6" /><path d="M0.8 2 L5 5.4 L9.2 2"/></svg>
        hello@lashvora-demo.com
      </li>
      <li class="contact__item">
        <svg class="contact__icon" viewBox="0 0 10 10" aria-hidden="true"><circle cx="5" cy="5" r="4.2"/><ellipse cx="5" cy="5" rx="1.8" ry="4.2"/><path d="M0.8 5 H9.2 M1.5 3 H8.5 M1.5 7 H8.5"/></svg>
        www.lashvorastudio-demo.com
      </li>
    </ul>

    <address class="address" style="font-style: normal;">
      6812 N.Calder Ridge Ave<br>
      Beverly Hills , CA 90210
    </address>
  </section>

  <section class="card card--back" aria-label="Business card back">
    <div class="brand">
      <span class="brand__name">Lashvora</span>
      <span class="brand__place">BEVERLY HILLS</span>
    </div>
  </section>

</main>
</body>
</html>
```